DELMORAN Auto Battery

We need top of the line design for a new product that we are launching, Automotive Batteries.
We are an exporter of Auto Spare parts based in China, our new products will be launched in October 2012, the website is to be presented as B2B not B2C, we deal directly with Importers all around the world.
Our vision for the website is to be Clean, elegant, smart, warm, reflects confidence and trust..therefore, the choice of themes, colors, fonts and graphics should take into considerations all above.
Since there are hundreds of Battery types, specs, sizes, weight...etc, we will need a upload template that will enable us to upload, modify and manipulate the data of the batteries.
Car battery importers
Automotive

```html
<!DOCTYPE html>
<html lang="en">
<head>
<meta charset="utf-8">
<title>DELMORAN Auto Battery</title>
<link rel="stylesheet" href="https://fonts.googleapis.com/css2?family=Arimo:wght@400;700&family=Oswald:wght@500;700&family=Cinzel:wght@700&display=swap">
<style>
:root{
  --canvas:#9c9c9c;
  --page:#ffffff;
  --ink:#222222;
  --muted:#777777;
  --line:#d6d6d6;
  --orange:#f26a1b;
  --orange-dark:#d45410;
  --red:#d3231b;
  --nav-top:#454545;
  --nav-bottom:#1f1f1f;
  --header:#ececec;
  --grid-bg:#efefef;
}
*{box-sizing:border-box;margin:0;padding:0}
html,body{width:700px;height:1200px;overflow:hidden}
body{background:var(--canvas);font-family:"Arimo",Arial,sans-serif;color:var(--ink);position:relative}
.page{position:absolute;left:19px;top:20px;width:662px;height:1180px;background:var(--page)}
/* header */
.site-header{position:absolute;left:0;top:0;width:662px;height:76px;background:linear-gradient(#f6f6f6,var(--header));border-bottom:1px solid var(--line)}
.account-links{position:absolute;right:14px;top:8px;font-size:9px;color:var(--red)}
.utility-links{position:absolute;right:14px;top:22px;font-size:9px;color:#555;display:flex;gap:10px}
.cart-tab{position:absolute;left:292px;top:44px;width:160px;height:26px;background:var(--orange);color:#fff;font-size:10px;font-weight:700;display:flex;align-items:center;justify-content:center;gap:6px;letter-spacing:.5px}
.search{position:absolute;left:456px;top:44px;width:196px;height:26px;background:#2a2a2a;display:flex;align-items:center;padding:0 6px;gap:8px}
.search span{color:#fff;font-size:11px;font-weight:700}
.search i{flex:1;height:16px;background:#fff;display:block}
/* nav */
.main-nav{position:absolute;left:0;top:76px;width:662px;height:50px;background:linear-gradient(var(--nav-top),var(--nav-bottom));display:flex;padding:0 14px}
.main-nav a{flex:1;color:#fff;text-decoration:none;font-size:10px;font-weight:700;line-height:12px;text-transform:uppercase;display:flex;align-items:center;justify-content:center;text-align:center;border-right:1px solid #555}
.main-nav a:last-child{border-right:0}
/* hero */
.hero{position:absolute;left:0;top:126px;width:662px;height:296px;background:radial-gradient(ellipse at 55% 55%,#4a4d52 0%,#1b1c1f 55%,#060606 100%)}
/* promos */
.promos{position:absolute;left:0;top:426px;width:662px;height:116px;display:flex;gap:4px;padding:0 4px}
.promo{position:relative;width:150px;height:116px;border:1px solid var(--line);background:#fff}
.promo h3{position:absolute;left:8px;top:8px;font-family:"Oswald",sans-serif;font-weight:500;font-size:15px;line-height:17px;color:var(--ink)}
.promo h3 em{display:block;font-style:normal;font-weight:700;font-size:20px;line-height:22px;color:var(--red)}
.promo .battery{position:absolute;right:6px;top:24px;width:72px;height:56px;border-radius:3px;background:linear-gradient(#3b3b3b,#101010)}
.promo .details{position:absolute;left:8px;bottom:8px;font-size:8px;color:#444;padding:3px 6px;border:1px solid #bbb;background:linear-gradient(#fff,#e5e5e5)}
.shipping{flex:1;height:116px;background:var(--orange);color:#fff;padding:10px 12px;font-family:"Cinzel",serif}
.shipping strong{display:block;font-size:34px;line-height:36px}
.shipping span{display:block;font-size:22px;line-height:24px}
.shipping p{font-family:"Arimo",sans-serif;font-size:7px;line-height:10px;margin-top:8px}
/* products */
.products{position:absolute;left:0;top:548px;width:662px;height:464px;background:var(--grid-bg);display:grid;grid-template-columns:repeat(4,1fr);gap:10px;padding:10px 12px}
.card{background:#fff;border:1px solid var(--line);border-radius:6px;position:relative}
.card h4{font-size:10px;font-weight:700;margin:10px 0 0 10px}
.card .spec{font-size:8px;color:var(--muted);margin:3px 0 0 10px}
.card .photo{position:absolute;left:20px;top:44px;width:112px;height:110px;border-radius:4px;background:radial-gradient(circle,#c9c9c9,#f7f7f7 70%)}
.card .photo.dark{background:radial-gradient(circle,#555,#eee 75%)}
.card .buy{position:absolute;left:10px;right:10px;bottom:10px;display:flex;justify-content:space-between;align-items:center;border-top:1px solid #eee;padding-top:6px}
.card .price{font-size:9px;color:var(--ink)}
.card .add{background:var(--orange);color:#fff;font-size:7px;font-weight:700;padding:4px 8px}
/* footer */
.site-footer{position:absolute;left:0;top:1014px;width:662px;height:166px;background:#fff;border-top:4px solid #e2e2e2}
.footer-cols{display:flex;padding:12px 30px 0}
.footer-cols div{flex:1}
.footer-cols h5{font-size:12px;font-weight:700;margin-bottom:8px}
.footer-cols a{display:block;font-size:9px;line-height:12px;color:#444;text-decoration:none}
.copyright{position:absolute;left:14px;bottom:14px;font-size:8px;color:var(--muted)}
</style>
</head>
<body>
<div class="page">
  <header class="site-header">
    <div class="account-links">Log in | Register</div>
    <nav class="utility-links"><span>Home</span><span>Site Cart</span><span>My Account</span><span>About Us</span><span>Contact Us</span></nav>
    <div class="cart-tab">
      <svg width="12" height="11" viewBox="0 0 12 11"><path d="M0 1h2l2 6h6l1.5-4.5H3" fill="none" stroke="#fff" stroke-width="1.3"/><circle cx="4.5" cy="9.5" r="1" fill="#fff"/><circle cx="9" cy="9.5" r="1" fill="#fff"/></svg>
      MY SHOPPING CART
    </div>
    <div class="search"><span>SEARCH</span><i></i></div>
  </header>

  <nav class="main-nav">
    <a href="#">Automotive<br>Batteries</a><a href="#">Automotive<br>Batteries</a><a href="#">Automotive<br>Batteries</a>
    <a href="#">Automotive<br>Batteries</a><a href="#">Automotive<br>Batteries</a><a href="#">Automotive<br>Batteries</a>
  </nav>

  <div class="hero" role="img" aria-label="Black sedan under studio light on a dark background"></div>

  <section class="promos">
    <div class="promo"><h3>Get Into<em>GEAR!</em></h3><div class="battery" role="img" aria-label="Car battery"></div><span class="details">View Details »</span></div>
    <div class="promo"><h3>Drive<em>SAFER!</em></h3><div class="battery" role="img" aria-label="Car battery"></div><span class="details">View Details »</span></div>
    <div class="promo"><h3>A Cleaner<em>CHOICE!</em></h3><div class="battery" role="img" aria-label="Car battery"></div><span class="details">View Details »</span></div>
    <div class="shipping"><strong>FREE</strong><span>Shipping</span><p>Free delivery on bulk importer orders worldwide.<br>Terms apply to selected battery lines only.</p></div>
  </section>

  <section class="products">
    <article class="card"><h4>Car Battery Name Here »</h4><p class="spec">( Battery specialization here)</p><div class="photo" role="img" aria-label="Headlight bulb set"></div><div class="buy"><span class="price">$ 200.00</span><span class="add">ADD TO CART</span></div></article>
    <article class="card"><h4>Car Battery Name Here »</h4><p class="spec">( Battery specialization here)</p><div class="photo" role="img" aria-label="Alternator"></div><div class="buy"><span class="price">$ 200.00</span><span class="add">ADD TO CART</span></div></article>
    <article class="card"><h4>Car Battery Name Here »</h4><p class="spec">( Battery specialization here)</p><div class="photo dark" role="img" aria-label="Electronic control unit"></div><div class="buy"><span class="price">$ 200.00</span><span class="add">ADD TO CART</span></div></article>
    <article class="card"><h4>Car Battery Name Here »</h4><p class="spec">( Battery specialization here)</p><div class="photo" role="img" aria-label="Exhaust pipe parts"></div><div class="buy"><span class="price">$ 200.00</span><span class="add">ADD TO CART</span></div></article>
    <article class="card"><h4>Car Battery Name Here »</h4><p class="spec">( Battery specialization here)</p><div class="photo" role="img" aria-label="Brake disc and caliper"></div><div class="buy"><span class="price">$ 200.00</span><span class="add">ADD TO CART</span></div></article>
    <article class="card"><h4>Car Battery Name Here »</h4><p class="spec">( Battery specialization here)</p><div class="photo" role="img" aria-label="Shock absorber"></div><div class="buy"><span class="price">$ 200.00</span><span class="add">ADD TO CART</span></div></article>
    <article class="card"><h4>Car Battery Name Here »</h4><p class="spec">( Battery specialization here)</p><div class="photo dark" role="img" aria-label="Car battery"></div><div class="buy"><span class="price">$ 200.00</span><span class="add">ADD TO CART</span></div></article>
    <article class="card"><h4>Car Battery Name Here »</h4><p class="spec">( Battery specialization here)</p><div class="photo dark" role="img" aria-label="Car battery"></div><div class="buy"><span class="price">$ 200.00</span><span class="add">ADD TO CART</span></div></article>
  </section>

  <footer class="site-footer">
    <div class="footer-cols">
      <div><h5>Information</h5><a href="#">About us</a><a href="#">Contact Us</a><a href="#">Why Us?</a><a href="#">Join Us</a></div>
      <div><h5>Our Services</h5><a href="#">Cars Battery</a><a href="#">Car Spare Parts</a><a href="#">Car interior</a><a href="#">Automotive Battery</a></div>
      <div><h5>Like Us On</h5><a href="#">Friendpage</a><a href="#">Chirpline</a><a href="#">Circleweb +</a><a href="#">Workround</a><a href="#">Email Us</a></div>
      <div><h5>Site Map</h5><a href="#">Home</a><a href="#">About Us</a><a href="#">Products</a><a href="#">Services</a></div>
    </div>
    <p class="copyright">Copyright DELMORAN, All Right Reserved</p>
  </footer>
</div>
</body>
</html>
```